Business Cards for Communications Technology Company

We are an innovative software company based in Tropical North Queensland, Australia. We have several brands with a focus on communications software for businesses. We are looking for a business card that is very innovate and creative whilst still remaining professional on a corporate level.

Our internal culture is very progressive and expresses a blend between the clarity of our natural surroundings and the highly technological industry we work in. Our current branding blends a modern minimalist typeface with the desire to push the boundaries in the way we communicate.

This is a corporate level business card for the communications software industry and may possibly also encompass our brands MarNetwork, PelFax, TukMailer and our B2B marketing service—with our companies name being Viresca Partners. Showing other brands on the business card is optional not compulsory.

Technical notes:

-We will attach all logo's and some examples of our corporate branding
- Would be willing to print with various papers, embossed, metallic ink, curved edges etc. in a standard business card size

Sample content:

Rowan Pellick
Senior Account Manager
Phone: 1300 842 916 / +617 4583 2764
Email: r.pellick@viresca.com.au
Web: www.viresca.com.au

Sincerely,
Viresca Partners.

```html
<!DOCTYPE html>
<html lang="en">
<head>
<meta charset="utf-8">
<title>Viresca Partners — Business Cards</title>
<link rel="stylesheet" href="https://fonts.googleapis.com/css2?family=Poppins:wght@400;500;600;700&display=swap">
<style>
  :root{
    --bg:#e6e6e6;
    --card:#ffffff;
    --green:#7dc142;
    --ink:#111111;
    --muted-line:#dcdcdc;
    --blue:#3a6fc4;
    --orange:#ee6a22;
    --shadow:0 10px 28px rgba(0,0,0,.18);
  }
  *{margin:0;padding:0;box-sizing:border-box}
  html,body{width:1200px;height:1000px;overflow:hidden}
  body{background:var(--bg);font-family:"Poppins",sans-serif;position:relative;color:var(--ink)}
  .card{position:absolute;background:var(--card);box-shadow:var(--shadow);overflow:hidden}
  .card svg.shapes{position:absolute;inset:0}

  /* back card */
  .card-back{left:440px;top:50px;width:700px;height:400px}
  .back-wordmark{position:absolute;left:36px;top:108px;display:flex;align-items:center;gap:10px;
    color:#fff;font-weight:600;font-size:26px;letter-spacing:.3px;white-space:nowrap}
  .back-wordmark .mark-dot{width:24px;height:24px;border-radius:50%;background:#fff;flex:none}
  .brand-list{position:absolute;right:46px;top:170px;display:flex;flex-direction:column;align-items:flex-end;gap:22px}
  .brand{display:flex;align-items:center;gap:10px;font-weight:600;font-size:24px}
  .brand .dot{width:16px;height:16px;border-radius:50%}
  .brand-fax{color:var(--green)} .brand-fax .dot{background:var(--green)}
  .brand-mail{color:var(--blue)} .brand-mail .dot{background:var(--blue)}
  .brand-net{color:var(--orange)} .brand-net .dot{background:var(--orange)}

  /* front card */
  .card-front{left:60px;top:500px;width:740px;height:430px}
  .person{position:absolute;left:52px;top:44px}
  .person-name{font-weight:700;font-size:29px;line-height:1.1;letter-spacing:.3px}
  .person-role{font-weight:500;font-size:16px;color:var(--green);margin-top:2px}
  .contact-group{position:absolute;left:52px;display:flex;gap:10px}
  .contact-group::before{content:"";width:4px;background:var(--green);border-radius:1px}
  .contact-group p{font-size:20px;line-height:1.2;font-weight:400}
  .contact-phone{top:222px}
  .contact-web{top:298px}
  .front-wordmark{position:absolute;left:460px;top:196px;display:flex;align-items:center;gap:10px;
    font-weight:600;font-size:26px;color:var(--ink);white-space:nowrap}
  .front-wordmark .mark-dot{width:24px;height:24px;border-radius:50%;background:var(--green);flex:none}
</style>
</head>
<body>

<section class="card card-back" aria-label="Card back">
  <svg class="shapes" width="700" height="400" viewBox="0 0 700 400" aria-hidden="true">
    <polygon points="0,0 410,0 250,400 0,400" fill="var(--green)"/>
  </svg>
  <div class="back-wordmark"><span class="mark-dot"></span>Viresca Partners</div>
  <div class="brand-list">
    <div class="brand brand-fax">PelFax<span class="dot"></span></div>
    <div class="brand brand-mail">TukMailer<span class="dot"></span></div>
    <div class="brand brand-net">MarNetwork<span class="dot"></span></div>
  </div>
</section>

<section class="card card-front" aria-label="Card front">
  <svg class="shapes" width="740" height="430" viewBox="0 0 740 430" aria-hidden="true">
    <polygon points="0,0 372,0 318,430 0,430" fill="#fdfdfd"/>
    <line x1="372" y1="0" x2="318" y2="430" stroke="var(--muted-line)" stroke-width="2"/>
    <polygon points="372,0 460,0 392,150" fill="var(--green)"/>
    <polygon points="350,220 410,220 404,262 345,262" fill="var(--green)"/>
    <g fill="none" stroke="#fff" stroke-width="2.2" stroke-linecap="round" stroke-linejoin="round">
      <path d="M366 238 q0 -8 12 -8 q12 0 12 8"/>
      <rect x="368" y="238" width="20" height="14" rx="3"/>
      <circle cx="378" cy="245" r="3"/>
    </g>
    <polygon points="341,288 401,288 395,330 336,330" fill="var(--green)"/>
    <g fill="none" stroke="#fff" stroke-width="2">
      <circle cx="368" cy="309" r="13"/>
      <ellipse cx="368" cy="309" rx="6" ry="13"/>
      <line x1="355" y1="309" x2="381" y2="309"/>
      <line x1="357" y1="302" x2="379" y2="302"/>
      <line x1="357" y1="316" x2="379" y2="316"/>
    </g>
  </svg>

  <div class="person">
    <h1 class="person-name">Rowan Pellick</h1>
    <p class="person-role">Senior Account Manager</p>
  </div>
  <div class="contact-group contact-phone">
    <div><p>1300 842 916</p><p>617 4583 2764</p></div>
  </div>
  <div class="contact-group contact-web">
    <div><p>r.pellick@viresca.com.au</p><p>www.viresca.com.au</p></div>
  </div>
  <div class="front-wordmark"><span class="mark-dot"></span>Viresca Partners</div>
</section>

</body>
</html>
```